Visitenkarten für ein Metallverarbeitsungsbetrieb
Zielgruppe
Metallverarbeitsungsbetrieb
spezialisiert auf Lasern
Aufgabenstellung
Passend zu unseren Logo und in den Farben, schlicht dennoch besonders

```html
<!DOCTYPE html>
<html lang="de">
<head>
<meta charset="utf-8">
<title>Visitenkarten – Ferrax Laser GmbH</title>
<link href="https://fonts.googleapis.com/css2?family=Montserrat:wght@500&family=Oswald:wght@300&display=swap" rel="stylesheet">
<style>
  :root {
    --backdrop: #cde3f0;
    --card-light: #ffffff;
    --card-dark: #0e0e11;
    --brand-blue: #0f7bb8;
    --text-grey: #6a6a6a;
    --wordmark-grey: #707070;
  }
  * { margin: 0; padding: 0; box-sizing: border-box; }
  html, body {
    width: 1200px;
    height: 1200px;
    overflow: hidden;
    background: var(--backdrop);
  }
  .canvas {
    position: relative;
    width: 1200px;
    height: 1200px;
  }
  .card {
    position: absolute;
    left: 217px;
    width: 766px;
    height: 437px;
  }
  .card--front { top: 137px; background: var(--card-light); }
  .card--back  { top: 625px; background: var(--card-dark); }

  .brand {
    position: absolute;
    display: flex;
    align-items: center;
    gap: 16px;
  }
  .card--front .brand { left: 384px; top: 140px; }
  .card--back .brand  { left: 362px; top: 282px; }
  .brand__mark {
    width: 34px;
    height: 34px;
    background: var(--brand-blue);
  }
  .brand__name {
    font-family: "Montserrat", sans-serif;
    font-weight: 500;
    font-size: 30px;
    color: var(--wordmark-grey);
    white-space: nowrap;
  }

  .contact {
    position: absolute;
    left: 38px;
    top: 330px;
    font-family: "Oswald", sans-serif;
    font-weight: 300;
  }
  .contact__bar {
    position: absolute;
    left: 0;
    top: 0;
    width: 8px;
    height: 62px;
    background: var(--brand-blue);
  }
  .contact__name {
    position: absolute;
    left: 18px;
    top: -8px;
    font-size: 27px;
    color: var(--brand-blue);
    white-space: nowrap;
  }
  .contact__line {
    position: absolute;
    top: 29px;
    font-size: 27px;
    color: var(--text-grey);
    white-space: nowrap;
  }
  .contact__role  { left: 18px; }
  .contact__phone { left: 228px; }
  .contact__divider {
    position: absolute;
    left: 388px;
    top: 31px;
    width: 2px;
    height: 32px;
    background: var(--brand-blue);
  }
  .contact__email { left: 407px; letter-spacing: 1.2px; }
</style>
</head>
<body>
<main class="canvas">
  <section class="card card--front">
    <div class="brand">
      <span class="brand__mark"></span>
      <span class="brand__name">Ferrax Laser GmbH</span>
    </div>
    <div class="contact">
      <span class="contact__bar"></span>
      <p class="contact__name">YOUR NAME</p>
      <p class="contact__line contact__role">Owner/President</p>
      <p class="contact__line contact__phone">P:(123) 456789</p>
      <span class="contact__divider"></span>
      <p class="contact__line contact__email">name@yourcompany.de</p>
    </div>
  </section>

  <section class="card card--back">
    <div class="brand">
      <span class="brand__mark"></span>
      <span class="brand__name">Ferrax Laser GmbH</span>
    </div>
  </section>
</main>
</body>
</html>
```